Business / Discount Card

Looking to create a 2 sided business card. Front side to say "Thanks for flying with Skyward Drifts" then have link to "In-Flight Photos, www.skywarddrifts-example.com.au, password: skyward" Back side of card to have company logo, phone number, facebook & instagram logo and #skywarddrifts. Also included on this side will be discount text "Book again and save 10%. Use discount code: skyward10"Round Corner Card Templates are attached. Please ensure dimensions are correct.Thanks,

Font styles to use
Sans Serif

Colors
33a6d7
ffffff
000000

Requirements
Must have
• Logo
• Blue, White and Black color scheme

```html
<!DOCTYPE html>
<html lang="en">
<head>
<meta charset="UTF-8">
<title>Skyward Drifts – Thank You Card</title>
<link rel="stylesheet" href="https://fonts.googleapis.com/css2?family=Questrial&display=swap">
<style>
  :root {
    --sky-blue: #33a6d7;
    --bright-cyan: #19b4dc;
    --deep-blue: #0f6fc0;
    --ink: #000000;
    --night: #1c1412;
    --slate: #2c2d30;
    --slate-light: #36373a;
    --paper: #f2f2f2;
    --white: #ffffff;
    --rule: #bcbcbc;
    --stage: #d9dadc;
  }
  * { box-sizing: border-box; margin: 0; padding: 0; }
  html, body {
    width: 1200px; height: 900px; overflow: hidden;
    background: var(--stage);
    font-family: "Questrial", "Century Gothic", sans-serif;
  }
  .canvas {
    position: relative; width: 1200px; height: 900px;
    display: flex; flex-direction: column; align-items: center;
    justify-content: center; gap: 40px;
  }
  .card {
    position: relative; width: 700px; height: 400px;
    border-radius: 18px; overflow: hidden;
    box-shadow: 0 10px 26px rgba(0,0,0,0.25);
  }

  /* Front side */
  .card--front { background: var(--paper); }
  .balloon-illustration {
    position: absolute; left: 70px; top: -8px; width: 235px; height: 265px;
    border-radius: 50% 50% 46% 46% / 55% 55% 45% 45%;
    background: linear-gradient(160deg, #2a2b2e 0%, #1d1e20 60%, #23404d 100%);
  }
  .checker-pattern {
    position: absolute; right: 0; top: 20px; width: 330px; height: 130px;
    background: linear-gradient(200deg, rgba(25,180,220,0.55) 0%, rgba(25,180,220,0.15) 70%, rgba(25,180,220,0) 100%);
  }
  .front-waves { position: absolute; inset: 0; width: 100%; height: 100%; }
  .thanks {
    position: absolute; left: 320px; top: 165px; width: 330px;
    color: var(--sky-blue); font-size: 29px; line-height: 1.08;
    letter-spacing: 0.5px; text-align: center;
  }
  .photo-access {
    position: absolute; right: 34px; bottom: 16px; text-align: right;
    color: var(--white);
  }
  .photo-access__label { font-size: 14px; letter-spacing: 0.6px; color: var(--sky-blue); margin-bottom: 3px; }
  .photo-access__url { font-size: 19px; letter-spacing: 0.6px; }

  /* Back side */
  .card--back {
    background: radial-gradient(ellipse at 40% 40%, var(--slate-light), var(--slate) 70%);
    color: var(--white);
  }
  .brand {
    position: absolute; left: 62px; top: 135px; width: 300px;
    display: flex; align-items: center; gap: 12px;
  }
  .brand__mark {
    width: 24px; height: 24px; border-radius: 50%;
    background: var(--bright-cyan); flex: none;
  }
  .brand__name { font-size: 36px; color: var(--bright-cyan); letter-spacing: 0.5px; white-space: nowrap; }
  .divider {
    position: absolute; left: 395px; top: 105px; width: 2px; height: 105px;
    background: var(--rule);
  }
  .contact { position: absolute; left: 425px; top: 110px; }
  .contact__icons { display: flex; gap: 12px; margin-bottom: 14px; }
  .icon {
    width: 28px; height: 28px; border-radius: 50%;
    background: var(--white); display: flex; align-items: center; justify-content: center;
  }
  .contact__line { font-size: 19px; line-height: 1.25; letter-spacing: 0.4px; }
  .offer {
    position: absolute; left: 0; right: 0; bottom: 42px; text-align: center;
    font-size: 20px; letter-spacing: 0.6px;
  }
</style>
</head>
<body>
<main class="canvas">

  <section class="card card--front" aria-label="Card front">
    <div class="balloon-illustration" role="img" aria-label="Illustration of a black hot-air balloon with blue checkered bands and an orange basket"></div>
    <div class="checker-pattern" role="img" aria-label="Decorative scattered blue checkered diamond pattern"></div>
    <svg class="front-waves" viewBox="0 0 700 400" preserveAspectRatio="none" aria-hidden="true">
      <defs>
        <linearGradient id="waveBlue" x1="0" x2="1" y1="0" y2="0">
          <stop offset="0" stop-color="#0f6fc0"/>
          <stop offset="1" stop-color="#5fb3dc"/>
        </linearGradient>
      </defs>
      <path d="M0 240 C40 290 120 312 230 312 C380 312 520 285 700 292 L700 400 L0 400 Z" fill="url(#waveBlue)"/>
      <path d="M110 400 C210 332 330 312 460 312 C580 312 650 322 700 330 L700 400 Z" fill="#ffffff"/>
      <path d="M130 400 C226 340 340 321 460 321 C580 321 650 331 700 339 L700 400 Z" fill="#1c1412"/>
    </svg>
    <p class="thanks">Thanks for flying with Skyward Drifts</p>
    <div class="photo-access">
      <p class="photo-access__label">In-Flight Photos &nbsp;|&nbsp; password: skyward</p>
      <p class="photo-access__url">www.skywarddrifts-example.com.au</p>
    </div>
  </section>

  <section class="card card--back" aria-label="Card back">
    <div class="brand">
      <span class="brand__mark" aria-hidden="true"></span>
      <span class="brand__name">Skyward Drifts</span>
    </div>
    <div class="divider" aria-hidden="true"></div>
    <div class="contact">
      <div class="contact__icons">
        <span class="icon" aria-label="Phone">
          <svg width="16" height="16" viewBox="0 0 24 24"><path d="M6.6 10.8a15 15 0 0 0 6.6 6.6l2.2-2.2a1 1 0 0 1 1-.25 11 11 0 0 0 3.6.6 1 1 0 0 1 1 1V20a1 1 0 0 1-1 1A17 17 0 0 1 3 4a1 1 0 0 1 1-1h3.5a1 1 0 0 1 1 1 11 11 0 0 0 .6 3.6 1 1 0 0 1-.25 1z" fill="#33a6d7"/></svg>
        </span>
        <span class="icon" aria-label="Message">
          <svg width="16" height="16" viewBox="0 0 24 24"><path d="M4 4h16a1 1 0 0 1 1 1v10a1 1 0 0 1-1 1H9l-5 4V5a1 1 0 0 1 1-1z" fill="#33a6d7"/></svg>
        </span>
        <span class="icon" aria-label="Photos">
          <svg width="16" height="16" viewBox="0 0 24 24"><rect x="3" y="5" width="18" height="14" rx="1.5" fill="none" stroke="#33a6d7" stroke-width="2"/><path d="M5 17l5-6 4 4 2-2 3 4z" fill="#33a6d7"/></svg>
        </span>
        <span class="icon" aria-label="Share">
          <svg width="16" height="16" viewBox="0 0 24 24"><circle cx="6" cy="12" r="3" fill="#33a6d7"/><circle cx="18" cy="6" r="3" fill="#33a6d7"/><circle cx="18" cy="18" r="3" fill="#33a6d7"/><path d="M6 12L18 6M6 12l12 6" stroke="#33a6d7" stroke-width="2"/></svg>
        </span>
      </div>
      <p class="contact__line">1300 555 019</p>
      <p class="contact__line">#skywarddrifts</p>
    </div>
    <p class="offer">Book again and save 10% &nbsp;/&nbsp; Use discount code:skyward10</p>
  </section>

</main>
</body>
</html>
```